Therapy Dog Business need a brochure

I need a brochure designed for my Canine Assisted Therapy business in Victoria Australia. I have a logo already and info and photos to upload.
Best as white background and using the colours from the logo please
Updates

Hi Everyone,
I am sorry to have to revise the brief. I have added three new photos I was unable to add due to the size. I have had to wait for my photographer to change the size to add them today. I have been really inspired by all the work you have done so far. Thank you.
Could you please add the following on the brochure. (Under the individual dogs photo)
1. Pebble is the white dog. Please add the following under her picture. Pebble is one of the first Court Dogs in Australia. Working in Victoria, she has worked in the following Courts. The Inquest Tribunal of Norvale, The Petty Sessions Bench in Collingwood, and the Shire Tribunal in Melbourne CBD. Her ability to use her intuition for clients is inspiring. Please contact us for potential use in Courts. Pebble has worked at the Halden Constabulary College, and at KESTREL at Hal Con. She is a stunning dog!
2. Tobias is the golden dog. Tobias is Pebbles son, and had her instinct of intuition of who needs his help. Tobias has an incredible soft approach as does his mother Pebble. He is incredibly safe with young children, and yet has a playful nature for adolescents and adults alike. He is soft and caring, and like his mother will go to those who need him most. Tobias like his mother has worked at Halden Constabulary, his time at HC included the Halden Constabulary Command (HCC) Both he and his mother have very impressive CV'S!
3. Clover the black dog. Clover is my Therapy and Assistance dog "trainer" she is safe and stable with all the dogs and people I train for Therapy Dog Training and Assistance Dog Training. She has also been with me on my journey as a Counsellor and I have been able to work alongside her and Pebble for Counselling sessions.
She is soft, caring, and also intuitive. I am incredibly grateful for her help, as well as Pebble and Tobias.
ALSO I am so sorry to add this but could you also add the following: Maybe in dot point?
Court Dog Availability
Therapy Dog Visits - Lawyers - Courts - Child Protection
Police Station / Ambulance Station / Fire Station - Visits
Private Therapy Dog Sessions
website and email confirmation coming soon. Thank you

Target Market(s)

First Responders

Requirements
Must have
• All the photos provided.
Should not have
• Generic photos

```html
<!DOCTYPE html>
<html lang="en">
<head>
<meta charset="utf-8">
<title>Hearthside Hounds – Canine Assisted Therapy Brochure</title>
<link href="https://fonts.googleapis.com/css2?family=Lilita+One&family=Arimo:wght@400;700&display=swap" rel="stylesheet">
<style>
:root{
  --maroon:#6a1d2d;
  --rust:#86372a;
  --orange:#f28a26;
  --pink:#e26b6b;
  --cream:#f7ede6;
  --white:#ffffff;
  --stage:#e8e8e8;
  --ink:#2b2020;
}
*{margin:0;padding:0;box-sizing:border-box}
html,body{width:1021px;height:1200px;overflow:hidden;background:var(--stage)}
body{position:relative;font-family:"Arimo",Arial,sans-serif;color:var(--ink)}
.display{font-family:"Lilita One","Arial Black",sans-serif;font-weight:400}
.page{position:absolute;width:364px;overflow:hidden;box-shadow:0 2px 6px rgba(0,0,0,.12)}
.page-why{left:138px;top:77px;height:514px;background:var(--white)}
.page-cover{left:533px;top:77px;height:514px;background:var(--cream)}
.page-benefits{left:138px;top:624px;height:504px;background:var(--cream)}
.page-dogs{left:533px;top:624px;height:504px;background:var(--white)}
.abs{position:absolute}
.accent{color:var(--orange)}
.brand-name{position:absolute;font-family:"Lilita One","Arial Black",sans-serif;text-align:center;line-height:1.05}

/* Why choose page */
.page-why .brand-name{left:12px;top:38px;width:108px;font-size:16px;color:var(--maroon)}
.why-title{left:132px;top:20px}
.why-title span{display:block;line-height:1.08}
.why-title .l1{font-size:27px;color:var(--orange);margin-bottom:2px}
.why-title .l2{font-size:21px;color:var(--maroon)}
.why-band{left:0;top:118px;width:364px;height:206px;background:var(--cream)}
.feature{position:absolute;left:20px;width:330px}
.feature svg{position:absolute;left:0;top:0}
.feature h3{margin-left:63px;font-size:14px;color:var(--maroon);line-height:1}
.feature p{margin-left:63px;margin-top:3px;font-size:8px;line-height:1.3;color:var(--ink)}
.join-band{left:0;top:322px;width:364px;height:192px;background:var(--maroon);color:var(--white);text-align:center}
.join-title{margin-top:26px;font-size:27px;line-height:1.1}
.join-copy{margin:10px 18px 0;font-size:9.2px;line-height:1.35;text-align:left}
.cta{position:absolute;height:38px;display:flex;align-items:center;justify-content:center;color:var(--white);font-size:17px;border-radius:4px 4px 0 0}
.cta-phone{left:52px;top:478px;width:246px;background:var(--orange)}

/* Cover page */
.cover-top{left:0;top:0;width:364px;height:250px;background:var(--rust)}
.page-cover .brand-name{left:107px;top:72px;width:152px;font-size:22px;color:var(--cream)}
.cover-photo{left:0;top:188px;width:364px;height:132px;background:linear-gradient(180deg,#8a9be0 0%,#6f80d2 55%,#c9b58c 100%)}
.cover-title{left:0;top:344px;width:364px;text-align:center;font-size:35px;line-height:1.08;color:var(--maroon)}
.cover-title span{color:var(--rust)}
.cover-sub{left:14px;top:424px;width:336px;text-align:center;font-size:14px;line-height:1.3;font-weight:700;color:var(--ink)}
.cta-web{left:58px;top:477px;width:248px;background:var(--maroon)}

/* Benefits page */
.hero-photo{left:0;top:0;width:364px;height:185px;background:linear-gradient(120deg,#5a4a3c 0%,#d8c1a2 45%,#f2e2cc 100%)}
.hero-note{left:8px;top:160px;width:348px;height:44px;background:var(--orange);border-radius:6px;color:var(--white);font-weight:700;font-size:7.3px;line-height:1.25;text-align:center;padding:6px 14px}
.benefits-title{left:12px;top:218px;font-size:18.5px;color:var(--maroon)}
.benefit{position:absolute;top:250px;width:110px;height:147px;border:1px dashed var(--rust);background:var(--white);text-align:center;padding:8px 5px}
.benefit h4{font-size:9.5px;line-height:1.1;margin-bottom:8px}
.benefit p{font-size:6.9px;line-height:1.22}
.benefit-1{left:12px}.benefit-1 h4{color:var(--maroon)}
.benefit-2{left:127px}.benefit-2 h4{color:var(--pink)}
.benefit-3{left:242px}.benefit-3 h4{color:var(--orange)}
.court-band{left:0;top:412px;width:364px;height:92px;background:var(--rust);text-align:center;color:var(--white)}
.court-band h2{margin-top:18px;font-size:18px;color:var(--orange)}
.court-band p{font-family:"Lilita One","Arial Black",sans-serif;font-size:11px;line-height:1.3;margin-top:3px}

/* Dogs page */
.dog-strip{position:absolute;left:0;width:364px;background:var(--cream)}
.dog-photo{position:absolute;border-radius:6px;box-shadow:4px 4px 0 var(--maroon);background:linear-gradient(180deg,#8fa0e2 0%,#7383d2 70%,#5d6cc0 100%)}
.dog-name{position:absolute;font-size:21px;color:var(--maroon);text-transform:uppercase;letter-spacing:.5px}
.dog-bio{position:absolute;font-size:6.5px;line-height:1.24;text-align:justify;color:var(--ink)}
</style>
</head>
<body>

<!-- Why choose -->
<section class="page page-why">
  <div class="brand-name">Hearthside<br>Hounds</div>
  <h1 class="abs why-title display"><span class="l1">Why Choose</span><span class="l2">Canine Assisted</span><span class="l2">Therapy?</span></h1>
  <div class="abs why-band"></div>

  <div class="feature" style="top:152px">
    <svg width="44" height="44" viewBox="0 0 44 44"><circle cx="20" cy="22" r="18" fill="none" stroke="var(--pink)" stroke-width="3"/><path d="M11 22l8 8 20-22" fill="none" stroke="var(--pink)" stroke-width="4" stroke-linecap="round" stroke-linejoin="round"/></svg>
    <h3 class="display">Proven <span class="accent">Effectiveness</span></h3>
    <p>Studies and testimonials highlight the positive effects therapy dogs have on emotional, psychological and physical health.</p>
  </div>
  <div class="feature" style="top:198px">
    <svg width="44" height="40" viewBox="0 0 44 40"><path d="M22 38C8 27 1 20 1 12 1 5 6 1 12 1c4 0 8 3 10 6 2-3 6-6 10-6 6 0 11 4 11 11 0 8-7 15-21 26z" fill="var(--pink)"/></svg>
    <h3 class="display">Non-Invasive and <span class="accent">Gentle</span></h3>
    <p>Therapy dogs provide a natural and non-threatening way to engage with patients, making it accessible for individuals who may feel apprehensive about traditional therapy methods.</p>
  </div>
  <div class="feature" style="top:256px">
    <svg width="44" height="46" viewBox="0 0 44 46"><path d="M20 2l17 6v13c0 11-8 19-17 23C11 40 3 32 3 21V8z" fill="none" stroke="var(--pink)" stroke-width="3"/><path d="M20 8l12 4v9c0 8-5 14-12 17-7-3-12-9-12-17v-9z" fill="var(--pink)"/><path d="M14 22l5 5 9-10" fill="none" stroke="var(--white)" stroke-width="3" stroke-linecap="round" stroke-linejoin="round"/></svg>
    <h3 class="display">Safe and <span class="accent">Trustworthy</span></h3>
    <p>All therapy dogs are carefully trained to work with professionals, ensuring that interactions are safe, beneficial, and appropriate for all individuals.</p>
  </div>

  <div class="abs join-band">
    <h2 class="join-title display">Join <span class="accent">the Healing<br>Journey</span> Today!</h2>
    <p class="join-copy">Whether you are seeking emotional support or mental health improvement, Canine Assisted Therapy offers a unique and compassionate approach to healing. Connect with us today to learn more about how a therapy dog can help enhance your life and well-being.</p>
  </div>
  <div class="cta cta-phone">Phone Number</div>
</section>

<!-- Cover -->
<section class="page page-cover">
  <div class="abs cover-top"></div>
  <div class="brand-name">Hearthside<br>Hounds</div>
  <div class="abs cover-photo" role="img" aria-label="Photo of the three therapy dogs, two pale Labradors and a black Labrador, resting on a blue couch"></div>
  <h1 class="abs cover-title display">Canine Assisted<br>Therapy <span>(CAT)</span></h1>
  <p class="abs cover-sub">A unique form of therapy that integrates trained therapy dogs into the healing process.</p>
  <div class="cta cta-web">www.website.com</div>
</section>

<!-- Benefits -->
<section class="page page-benefits">
  <div class="abs hero-photo" role="img" aria-label="Photo of a smiling woman hugging a pale Labrador therapy dog"></div>
  <p class="abs hero-note">By working alongside licensed therapists, these compassionate and well-trained dogs help support individuals in overcoming emotional, physical, and psychological challenges. This innovative approach promotes healing, reduces stress, and enhances overall well-being.</p>
  <h2 class="abs benefits-title display"><span class="accent">Benefits</span> of Canine Assisted Therapy</h2>

  <div class="benefit benefit-1">
    <h4 class="display">Emotional Support and Comfort.</h4>
    <p>Therapy dogs provide immediate emotional support, offering comfort and companionship during therapy sessions. Their calming presence helps reduce feelings of anxiety, stress, depression, and grief, creating a safe and nurturing environment for healing.</p>
  </div>
  <div class="benefit benefit-2">
    <h4 class="display">Stress Relief and Relaxation</h4>
    <p>Interacting with dogs has been proven to reduce cortisol (stress hormone) levels and increase serotonin and oxytocin, the "feel-good" hormones. This natural relief from stress makes Canine Assisted Therapy an ideal option for individuals dealing with anxiety, trauma, PTSD, and grief.</p>
  </div>
  <div class="benefit benefit-3">
    <h4 class="display">Improved Mental Health.</h4>
    <p>Therapy dogs encourage social interaction, communication, and emotional expression, helping individuals address mental health challenges such as depression, anxiety, PTSD, and grief. The unconditional love and companionship of a dog can foster trust and openness during therapy sessions.</p>
  </div>

  <div class="abs court-band">
    <h2 class="display">Court Dog Availability</h2>
    <p>Therapy Dog Visits - Lawyers - Courts - Child Protection<br>Police Station / Ambulance Station / Fire Station - Visits<br>Private Therapy Dog Sessions</p>
  </div>
</section>

<!-- Dogs -->
<section class="page page-dogs">
  <div class="dog-strip" style="top:160px;height:176px"></div>

  <div class="dog-photo" style="left:13px;top:13px;width:148px;height:124px" role="img" aria-label="Photo of Pebble, a white Labrador lying on a blue couch"></div>
  <h2 class="dog-name display" style="left:228px;top:20px">Pebble</h2>
  <p class="dog-bio" style="left:178px;top:54px;width:171px">Pebble is the white dog. Pebble is one of the first Court Dogs in Australia. Working in Victoria, she has worked in the following Courts. The Inquest Tribunal of Norvale, The Petty Sessions Bench in Collingwood, and the Shire Tribunal in Melbourne CBD. Her ability to use her intuition for clients is inspiring. Please contact us for potential use in Courts. Pebble has worked at the Halden Constabulary College, and at KESTREL at Hal Con. She is a stunning dog!</p>

  <h2 class="dog-name display" style="left:40px;top:189px">Tobias</h2>
  <p class="dog-bio" style="left:17px;top:222px;width:162px">Tobias is the golden dog. Tobias is Pebbles son, and had her instinct of intuition of who needs his help. Tobias has an incredible soft approach as does his mother Pebble. He is incredibly safe with young children, and yet has a playful nature for adolescents and adults alike. He is soft and caring, and like his mother will go to those who need him most. Tobias like his mother has worked at Halden Constabulary, his time at HC included the Halden Constabulary Command (HCC) Both he and his mother have very impressive CV'S!</p>
  <div class="dog-photo" style="left:190px;top:180px;width:160px;height:130px" role="img" aria-label="Photo of Tobias, a golden Labrador sitting on a blue couch"></div>

  <div class="dog-photo" style="left:13px;top:351px;width:154px;height:127px" role="img" aria-label="Photo of Clover, a black Labrador lying on a blue couch"></div>
  <h2 class="dog-name display" style="left:226px;top:357px">Clover</h2>
  <p class="dog-bio" style="left:190px;top:390px;width:160px">Clover the black dog. Clover is my Therapy and Assistance dog "trainer" she is safe and stable with all the dogs and people I train for Therapy Dog Training and Assistance Dog Training. She has also been with me on my journey as a Counsellor and I have been able to work alongside her and Pebble for Counselling sessions. She is soft, caring, and also intuitive. I am incredibly grateful for her help, as well as Pebble and Tobias.</p>
</section>

</body>
</html>
```